Business Cards + Letterhead for Software Development/Consulting Company
Practical Veltrane Orbis KPX Specialists
I need double sided standard sized Business Card [3.5" x 2"]
I like Segoe. Logo used in Logo is Fontin Sans
Professional
Torvald Ramsdal
President
2417 Quintara Ave
Glendale, CA 90871
torvald@ramsdal.example
I would not be opposed to use a special shape (http://cardmillvex.example/g/specialshape.do) especially the wink shape!
My printer have templates provided also: http://cardmillvex.example/g/showStaticPage.do?page=download_templates-bc.html
I envision a black background with the logo.
Logo (White Background) as received from Logo Contest Winner
Logo (Black Background) as received from Logo Contest Winner
Me - if you want to make a card with my picture on it

```html
<!DOCTYPE html>
<html lang="en">
<head>
<meta charset="utf-8">
<title>Ramsdal Consulting – Stationery</title>
<link href="https://fonts.googleapis.com/css2?family=Open+Sans:wght@400;600;700&display=swap" rel="stylesheet">
<style>
  :root{
    --bg:#e4e6e9;
    --paper:#ffffff;
    --ink:#3d3f42;
    --muted:#8a8d91;
    --rule:#c9ccd0;
    --black:#111214;
    --green:#6cb33f;
    --blue:#2a7fc1;
    --sky:#5fb3e6;
    --shadow:0 2px 6px rgba(0,0,0,.18);
  }
  *{box-sizing:border-box;margin:0;padding:0}
  html,body{width:1200px;height:614px;overflow:hidden}
  body{background:var(--bg);font-family:"Open Sans",Arial,sans-serif;color:var(--ink);position:relative}

  .brand{display:flex;align-items:center;gap:5px;font-weight:700;color:var(--ink);line-height:1.05;letter-spacing:.02em}
  .brand__mark{background:var(--green);flex:none}
  .brand--light{color:#ffffff}

  /* Envelopes */
  .envelope{position:absolute;width:360px;height:156px;background:var(--paper);box-shadow:var(--shadow)}
  .envelope--back{left:40px;top:40px;overflow:hidden}
  .envelope__flap{position:absolute;inset:0}
  .envelope--back .brand{position:absolute;left:50%;top:30px;transform:translateX(-50%);font-size:8px;white-space:nowrap}
  .envelope--back .brand__mark{width:9px;height:9px}
  .envelope--front{left:40px;top:216px;padding:16px 18px}
  .envelope--front .brand{font-size:10px}
  .envelope--front .brand__mark{width:12px;height:12px}
  .return-address{font-size:6px;color:var(--muted);margin-top:4px;line-height:1.4}

  /* Business cards */
  .card{position:absolute;top:410px;width:175px;height:100px;border-radius:8px;background:var(--black);box-shadow:var(--shadow);overflow:hidden}
  .card--front{left:40px;display:flex;align-items:center;justify-content:center}
  .card--front .brand{font-size:11px}
  .card--front .brand__mark{width:14px;height:14px}
  .card--back{left:225px;padding:9px 10px}
  .card__info{position:relative;z-index:1;width:82px}
  .card--back .brand{font-size:6.5px}
  .card--back .brand__mark{width:9px;height:9px}
  .card__portrait{position:absolute;right:0;bottom:0;width:80px;height:100px;background:radial-gradient(ellipse at 55% 45%,#6f8fb4 0%,#2a3e5b 55%,#0d1420 100%)}
  .card__person{margin-top:8px;font-size:7px;font-weight:700;color:var(--sky);white-space:nowrap}
  .card__role{font-size:5.5px;color:#ffffff;margin-bottom:4px}
  .card__details{font-size:5px;color:#d6dbe1;line-height:1.45;white-space:nowrap}

  /* Sheets */
  .sheet{position:absolute;top:87px;width:340px;height:440px;background:var(--paper);box-shadow:var(--shadow);padding:26px 26px}
  .sheet--letter{left:440px}
  .sheet--fax{left:820px}
  .sheet__head{display:flex;justify-content:space-between;align-items:flex-start}
  .sheet .brand{font-size:10px}
  .sheet .brand__mark{width:13px;height:13px}
  .sheet__contact{display:flex;gap:10px;font-size:5px;color:var(--muted);line-height:1.45}

  .fax__title{text-align:right;font-size:9px;font-weight:700;letter-spacing:.12em;margin-top:8px}
  .fax__grid{margin-top:6px;width:100%;border-collapse:collapse;font-size:6px}
  .fax__grid td{border:1px solid var(--rule);height:15px;padding:0 4px;color:var(--ink)}
  .fax__grid td.label{width:32px;background:#f3f4f6;font-weight:600}
  .fax__checks{display:flex;justify-content:space-between;margin-top:9px;font-size:5.5px}
  .fax__checks span::before{content:"";display:inline-block;width:5px;height:5px;border:1px solid var(--ink);margin-right:3px;vertical-align:-1px}
</style>
</head>
<body>

  <div class="envelope envelope--back">
    <svg class="envelope__flap" width="360" height="156" viewBox="0 0 360 156" aria-hidden="true">
      <path d="M0 0 H360 L200 74 Q180 82 160 74 Z" fill="#111214"/>
    </svg>
    <div class="brand brand--light"><span class="brand__mark"></span>RAMSDAL CONSULTING, INC.</div>
  </div>

  <div class="envelope envelope--front">
    <div class="brand"><span class="brand__mark"></span>RAMSDAL CONSULTING, INC.</div>
    <p class="return-address">2417 Quintara Ave<br>Glendale, CA 90871</p>
  </div>

  <div class="card card--front">
    <div class="brand brand--light"><span class="brand__mark"></span>RAMSDAL</div>
  </div>

  <div class="card card--back">
    <div class="card__portrait" role="img" aria-label="Portrait photograph of Torvald Ramsdal"></div>
    <div class="card__info">
      <div class="brand brand--light"><span class="brand__mark"></span>RAMSDAL<br>CONSULTING, INC.</div>
      <p class="card__person">Torvald Ramsdal</p>
      <p class="card__role">President</p>
      <p class="card__details">2417 Quintara Ave<br>Glendale, CA 90871<br>Tel 818-555-0142<br>Mobile 818-555-0199<br>torvald@ramsdal.example</p>
    </div>
  </div>

  <div class="sheet sheet--letter">
    <div class="sheet__head">
      <div class="brand"><span class="brand__mark"></span>RAMSDAL<br>CONSULTING, INC.</div>
      <div class="sheet__contact">
        <p>2417 Quintara Ave<br>Glendale, CA 90871</p>
        <p>Tel 818-555-0142<br>Fax 818-555-0143<br>torvald@ramsdal.example</p>
      </div>
    </div>
  </div>

  <div class="sheet sheet--fax">
    <div class="sheet__head">
      <div class="brand"><span class="brand__mark"></span>RAMSDAL<br>CONSULTING, INC.</div>
      <div class="sheet__contact">
        <p>2417 Quintara Ave<br>Glendale, CA 90871</p>
        <p>Tel 818-555-0142<br>Fax 818-555-0143<br>torvald@ramsdal.example</p>
      </div>
    </div>
    <p class="fax__title">FAX</p>
    <table class="fax__grid">
      <tr><td class="label">To</td><td></td><td class="label">From</td><td></td></tr>
      <tr><td class="label">Fax</td><td></td><td class="label">Pages</td><td></td></tr>
      <tr><td class="label">Phone</td><td></td><td class="label">Date</td><td></td></tr>
      <tr><td class="label">Re</td><td></td><td class="label">CC</td><td></td></tr>
    </table>
    <div class="fax__checks">
      <span>Urgent</span><span>For Review</span><span>Please Comment</span><span>Please Reply</span><span>Please Recycle</span>
    </div>
  </div>

</body>
</html>
```